Business Card Design

Contact Information for Business Card

A vertical business card request- a medium & light gray with silverfern tree logo (logo is attached)

Please use Trebuchet font -- if possible- can we use two different color gray? (See pictures attached below)
Info on the front should be the Silverfern tree logo - on the top of the card, followed by the info ...
Card to read: " " indicated what should be on the card --
Name: " Joan Pelley "
Title : "Partner "
" Office: 202.555.0147 "
" Mobile: 202.555.0182 "

Backside of the card - solid medium color gray color w/ address and small message centered in the card - Trebuchet font
to read:

" 317 B North Linden Avenue, NE "
" Washington, DC 20099 "

Then below address to read:
" Fundraising | Event Planning | Political Consulting "

```html
<!DOCTYPE html>
<html lang="en">
<head>
<meta charset="utf-8">
<title>Silverfern Strategies – Business Card</title>
<link href="https://fonts.googleapis.com/css2?family=Fira+Sans:wght@300;400&family=Fira+Sans+Condensed:wght@400&display=swap" rel="stylesheet">
<style>
  :root {
    --backdrop: #cbcbcb;
    --card-gray: #6f6e6c;
    --ink-light: #f4f4f2;
    --ink-soft: #e2e1df;
    --mark-faint: #7d7c7a;
    --card-shadow: rgba(0, 0, 0, 0.28);
  }
  * { box-sizing: border-box; margin: 0; padding: 0; }
  html, body {
    width: 1200px;
    height: 1005px;
    overflow: hidden;
    background: var(--backdrop);
  }
  .sheet {
    width: 1200px;
    height: 1005px;
    display: flex;
    justify-content: center;
    align-items: center;
    gap: 60px;
  }
  .card {
    width: 400px;
    height: 700px;
    background: var(--card-gray);
    box-shadow: 0 6px 14px var(--card-shadow);
    color: var(--ink-light);
    font-family: "Fira Sans", sans-serif;
    font-weight: 300;
    text-align: center;
    position: relative;
    overflow: hidden;
  }
  /* Front */
  .brand-mark {
    position: absolute;
    top: 105px;
    left: 50%;
    width: 150px;
    height: 150px;
    margin-left: -75px;
    border-radius: 50%;
    background: var(--ink-light);
  }
  .brand {
    position: absolute;
    top: 275px;
    left: 0;
    right: 0;
    color: var(--ink-light);
    text-transform: uppercase;
  }
  .brand-name {
    display: block;
    font-size: 38px;
    letter-spacing: 2px;
    line-height: 1;
  }
  .brand-tag {
    display: block;
    font-size: 18px;
    letter-spacing: 3px;
    margin-top: 6px;
    padding-left: 150px;
  }
  .address {
    position: absolute;
    top: 515px;
    left: 0;
    right: 0;
    font-size: 18px;
    line-height: 1.4;
    color: var(--ink-soft);
  }
  .services {
    position: absolute;
    top: 600px;
    left: 0;
    right: 0;
    font-family: "Fira Sans Condensed", sans-serif;
    font-weight: 400;
    font-size: 17px;
    color: var(--ink-soft);
  }
  .services .divider { margin: 0 6px; }
  /* Back */
  .brand-mark-faint {
    position: absolute;
    top: 170px;
    left: 50%;
    width: 250px;
    height: 250px;
    margin-left: -125px;
    border-radius: 50%;
    background: var(--mark-faint);
  }
  .contact {
    position: absolute;
    top: 210px;
    left: 0;
    right: 0;
  }
  .person-name {
    font-size: 26px;
    font-weight: 400;
  }
  .person-title {
    font-size: 17px;
    margin-top: 2px;
    color: var(--ink-soft);
  }
  .contact-lines {
    list-style: none;
    margin-top: 40px;
    font-size: 18px;
    line-height: 1.45;
    color: var(--ink-soft);
    letter-spacing: 0.5px;
  }
</style>
</head>
<body>
  <main class="sheet">
    <section class="card card-front" aria-label="Card front">
      <div class="brand-mark" role="img" aria-label="Silverfern Strategies brand mark"></div>
      <div class="brand">
        <span class="brand-name">Silverfern</span>
        <span class="brand-tag">Strategies</span>
      </div>
      <p class="address">317 B North Linden Avenue, NE<br>Washington, DC 20099</p>
      <p class="services">Fundraising<span class="divider">|</span>Event Planning<span class="divider">|</span>Political Consulting</p>
    </section>

    <section class="card card-back" aria-label="Card back">
      <div class="brand-mark-faint" role="img" aria-label="Faint Silverfern brand mark behind contact details"></div>
      <div class="contact">
        <h1 class="person-name">Joan Pelley</h1>
        <p class="person-title">Partner</p>
        <ul class="contact-lines">
          <li>202.555.0147</li>
          <li>202.555.0182</li>
          <li>joan@silverfernllc.com</li>
          <li>www.silverfernllc.com</li>
        </ul>
      </div>
    </section>
  </main>
</body>
</html>
```